Quillmere Harbor Partners

Please look at the logo that we've just received and based on it provide us with the business card designs.

Industry/Entity Type

Business

Requirements
Must have
• Dummy text, so later on we can add the exact names and titles.

```html
<!DOCTYPE html>
<html lang="en">
<head>
<meta charset="utf-8">
<title>Quillmere Harbor Partners – Business Card</title>
<link rel="stylesheet" href="https://fonts.googleapis.com/css2?family=Lato:wght@400;700&display=swap">
<style>
  :root {
    --page-bg: #2a2a2b;
    --card-bg: #1c1c1d;
    --card-edge: #262627;
    --brand-blue: #1f63c4;
    --text-light: #d4d4d6;
    --text-muted: #8a8a8e;
    --front-mark: #58585c;
  }
  * { margin: 0; padding: 0; box-sizing: border-box; }
  html, body {
    width: 1200px;
    height: 716px;
    overflow: hidden;
    background: var(--page-bg);
    font-family: "Lato", Arial, sans-serif;
  }
  .canvas {
    position: relative;
    width: 1200px;
    height: 716px;
    display: flex;
    align-items: center;
    justify-content: center;
    gap: 60px;
  }
  .card {
    position: relative;
    width: 500px;
    height: 286px;
    background: var(--card-bg);
    border: 1px solid var(--card-edge);
    border-radius: 18px;
    overflow: hidden;
    box-shadow: 0 14px 30px rgba(0,0,0,0.45);
  }

  /* Front */
  .card-front {
    display: flex;
    align-items: center;
    justify-content: center;
  }
  .front-brand {
    display: flex;
    align-items: center;
    gap: 14px;
  }
  .front-brand__square {
    width: 26px;
    height: 26px;
    background: var(--front-mark);
  }
  .front-brand__name {
    font-size: 26px;
    font-weight: 400;
    color: var(--front-mark);
    letter-spacing: 1px;
  }

  /* Back */
  .identity {
    position: absolute;
    left: 30px;
    top: 28px;
    display: flex;
    gap: 10px;
  }
  .identity__bar {
    width: 9px;
    height: 46px;
    background: var(--brand-blue);
  }
  .identity__name {
    font-size: 24px;
    color: var(--text-light);
    line-height: 1.1;
  }
  .identity__title {
    font-size: 13px;
    color: var(--brand-blue);
    margin-top: 2px;
  }
  .back-brand {
    position: absolute;
    right: 28px;
    top: 112px;
    display: flex;
    align-items: center;
    gap: 10px;
  }
  .back-brand__square {
    width: 18px;
    height: 18px;
    background: var(--brand-blue);
  }
  .back-brand__name {
    font-size: 17px;
    font-weight: 400;
    color: var(--brand-blue);
  }
  .contact-list {
    position: absolute;
    left: 30px;
    top: 150px;
    list-style: none;
  }
  .contact-list li {
    display: flex;
    align-items: center;
    gap: 10px;
    font-size: 15px;
    color: var(--text-light);
    height: 24px;
  }
  .contact-list svg { width: 14px; height: 14px; fill: var(--brand-blue); }
  .accent-rule {
    position: absolute;
    left: 0;
    top: 232px;
    width: 330px;
    height: 3px;
    background: var(--brand-blue);
  }
  .website {
    position: absolute;
    right: 28px;
    bottom: 22px;
    font-size: 13px;
    color: var(--text-muted);
    letter-spacing: 0.5px;
  }
</style>
</head>
<body>
<main class="canvas">
  <section class="card card-front" aria-label="Card front">
    <div class="front-brand">
      <span class="front-brand__square"></span>
      <span class="front-brand__name">Quillmere Harbor Partners</span>
    </div>
  </section>

  <section class="card card-back" aria-label="Card back">
    <div class="identity">
      <span class="identity__bar"></span>
      <div>
        <div class="identity__name">Your Name</div>
        <div class="identity__title">Job Title</div>
      </div>
    </div>

    <div class="back-brand">
      <span class="back-brand__square"></span>
      <span class="back-brand__name">Quillmere Harbor Partners</span>
    </div>

    <ul class="contact-list">
      <li>
        <svg viewBox="0 0 24 24" aria-hidden="true"><path d="M6.6 10.8a15.1 15.1 0 0 0 6.6 6.6l2.2-2.2c.3-.3.7-.4 1-.2 1.1.4 2.3.6 3.6.6.6 0 1 .4 1 1V20c0 .6-.4 1-1 1A17 17 0 0 1 3 4c0-.6.4-1 1-1h3.5c.6 0 1 .4 1 1 0 1.3.2 2.5.6 3.6.1.3 0 .7-.2 1z"/></svg>
        000 000 0000
      </li>
      <li>
        <svg viewBox="0 0 24 24" aria-hidden="true"><path d="M2 5h20v14H2zm2 2v.5l8 5 8-5V7l-8 5z"/></svg>
        youremail@xyz.com
      </li>
      <li>
        <svg viewBox="0 0 24 24" aria-hidden="true"><path d="M12 2a7 7 0 0 0-7 7c0 5 7 13 7 13s7-8 7-13a7 7 0 0 0-7-7zm0 9.5A2.5 2.5 0 1 1 12 6.5a2.5 2.5 0 0 1 0 5z"/></svg>
        youraddress, here 0000
      </li>
    </ul>

    <div class="accent-rule"></div>

    <div class="website">www.yourwebsite.com</div>
  </section>
</main>
</body>
</html>
```